Non-Profit focusing on clean water needs a poster/flyer design for our annual Stroll 2 Rivers

We need a poster and flyer design for our annual Stroll 2 Rivers event which will be held on Saturday, March 21st (Earthwide Thirst Day) at Merrow Fern Gardens.

HEAD:

Think Globally, Walk Locally.

SUB:

Join K7U in Santa Barbara on Earthwide Thirst Day for a Stroll 2 Rivers.

PHOTOS:

(one photo of past walk – crowd scene but with one face standing out – smaller photos of our team working out of country)

SUB:

Saturday, March 21st, 10am - 2pm

HEAD

Merrow Fern Gardens, Santa Barbara

COPY:

For more info check out our website: www.brightwellaid.org, or contact our Director: dana@brightwellaid.org; 805 382 9046

K7U Logo with Tag Line

NOTHING ELSE.

The final design should communicate fun for the whole family. Blue-ish shades to denote water. Be the generation that solves the world's water crisis.

Also, no need to use the attached photos if you can come up with a cool big idea graphic.

```html
<!DOCTYPE html>
<html lang="en">
<head>
<meta charset="utf-8">
<title>Think Globally, Walk Locally – Stroll 2 Rivers</title>
<link rel="stylesheet" href="https://fonts.googleapis.com/css2?family=Source+Sans+3:wght@400;600;700&display=swap">
<style>
  :root {
    --page: #ffffff;
    --sky-top: #d3eaf6;
    --sky-bottom: #bfe0f1;
    --wave-light: #5ec1ea;
    --wave-mid: #2f9bd9;
    --wave-deep: #0f6db6;
    --head-light: #2a8bd1;
    --head-dark: #1566ab;
    --ink-blue: #14589a;
    --white: #ffffff;
    --earth-light: #c3b19a;
    --earth-dark: #8b7a68;
  }
  * { margin: 0; padding: 0; box-sizing: border-box; }
  html, body { width: 1200px; height: 900px; overflow: hidden; background: var(--page); }
  body { font-family: "Source Sans 3", "Myriad Pro", sans-serif; }

  .poster {
    position: absolute; left: 253px; top: 0;
    width: 695px; height: 900px; overflow: hidden;
  }
  .poster-art { position: absolute; inset: 0; }

  .headline {
    position: absolute; left: 38px; top: 26px;
    font-weight: 700; font-size: 92px; line-height: 77px;
    letter-spacing: -1px; text-transform: uppercase;
  }
  .headline .think { color: var(--head-light); display: block; }
  .headline .walk { color: var(--head-dark); display: block; }

  .invite {
    position: absolute; left: 38px; top: 374px;
    font-size: 22px; line-height: 27px; color: var(--ink-blue);
  }
  .invite strong, .event-details strong { font-weight: 700; }

  .event-details {
    position: absolute; left: 38px; top: 560px;
    font-size: 22px; line-height: 24px; color: var(--white);
  }

  .org-mark {
    position: absolute; left: 70px; top: 722px;
    display: flex; align-items: center; gap: 14px;
  }
  .org-dot {
    width: 22px; height: 22px; border-radius: 50%;
    background: var(--white);
  }
  .org-name {
    font-weight: 700; font-size: 54px; line-height: 60px;
    color: var(--white); letter-spacing: 1px;
  }
  .tagline {
    position: absolute; left: 38px; top: 838px;
    font-size: 20px; color: var(--white);
  }

  .contact {
    position: absolute; left: 340px; top: 750px;
    font-size: 18.5px; line-height: 24px; color: var(--white);
  }
  .contact strong { font-weight: 700; }
</style>
</head>
<body>
  <main class="poster">
    <svg class="poster-art" width="695" height="900" viewBox="0 0 695 900">
      <defs>
        <linearGradient id="sky" x1="0" y1="0" x2="0" y2="1">
          <stop offset="0" stop-color="#d3eaf6"/>
          <stop offset="1" stop-color="#bfe0f1"/>
        </linearGradient>
        <linearGradient id="earth" x1="0" y1="0" x2="1" y2="1">
          <stop offset="0" stop-color="#c3b19a"/>
          <stop offset="1" stop-color="#8b7a68"/>
        </linearGradient>
      </defs>
      <rect class="sky" width="695" height="900" fill="url(#sky)"/>
      <path class="wave wave-light" d="M0,362 C110,338 230,345 360,382 C470,412 590,380 695,360 L695,900 L0,900 Z" fill="#5ec1ea"/>
      <path class="wave wave-mid" d="M0,522 C120,492 250,505 380,540 C480,565 590,545 695,520 L695,900 L0,900 Z" fill="#2f9bd9"/>
      <path class="photo-drop" role="img" aria-label="Photo of young volunteers in blue shirts digging a water trench with shovels"
            d="M589,172 L695,268 L695,735 L420,735 C365,690 338,610 344,535 C352,445 420,370 492,288 Z" fill="url(#earth)"/>
      <path class="wave wave-deep" d="M0,705 C130,680 270,685 400,710 C500,728 600,710 695,690 L695,900 L0,900 Z" fill="#0f6db6"/>
    </svg>

    <h1 class="headline">
      <span class="think">Think<br>Globally,</span>
      <span class="walk">Walk<br>Locally.</span>
    </h1>

    <p class="invite">
      <strong>Join K7U</strong> in<br>
      Santa Barbara on<br>
      <strong>Earthwide Thirst Day</strong><br>
      for a <strong>Stroll 2 Rivers.</strong>
    </p>

    <p class="event-details">
      <strong>Saturday, March 21st,</strong><br>
      10am - 2pm<br>
      <strong>Merrow Fern Gardens,</strong><br>
      Santa Barbara
    </p>

    <div class="org-mark"><span class="org-dot"></span><span class="org-name">K7U</span></div>
    <p class="tagline">A Movement of Young People</p>

    <p class="contact">
      For more info check out our website:<br>
      <strong>www.brightwellaid.org,</strong><br>
      or contact our Director:<br>
      <strong>dana@brightwellaid.org;</strong><br>
      <strong>805 382 9046</strong>
    </p>
  </main>
</body>
</html>
```